Word Template for KESTREL Polls

KESTREL Polls stands for 'Kinship Evaluation Study Tracking Regional Everyday Lives Polls'. It is a collaborative research effort to format and combine multiple sources of public opinion data from around the world into merged datasets. We need a Microsoft Word template design for our research reports, dataset codebooks, crowdsourced development guidelines, and other documents that will be produced as part of the research and development. The template should match the website design and logo, which are attached to this contest (these are the files from previous successful design contests).

The main purpose will be to write reports discussing research and analysis. There will be lots data visualizations (bar charts, scatter plots, pie charts, histograms, trend line charts etc.) as well as tables, diargams, and photos mixed in wit all the text. A second purpose will be to write guidebooks to describe processes and teach others how to manage data, find variables, and write code, which will include screenshots and Word are diagrams and figures.

There are some document uploaded as examples for the kinds of things for which we need the template (working papers, codebooks, pamphlets, etc)

Target Market(s)

academia, government, non-profits, postgraduates, researchers

Font styles to use
Serif

Colors

Designer to choose colors to be used in the design.

Requirements
Must have
• A4 size page template
• Cover page
• Must match website design and logo (see attached)
Nice to have
• Colors to match logo and website (see attached)

```html
<!DOCTYPE html>
<html lang="en">
<head>
<meta charset="utf-8">
<title>KESTREL Polls – Word Template</title>
<link href="https://fonts.googleapis.com/css2?family=Open+Sans:wght@300;400;600;700&display=swap" rel="stylesheet">
<style>
  :root{
    --bg:#c8c8c8;
    --page:#ffffff;
    --blue:#1774c5;
    --blue-dark:#0f5ea6;
    --blue-light:#2aa4e2;
    --ink:#2b2b2b;
    --muted:#555;
    --label:#3a3a3a;
    --row-alt:#efefef;
  }
  *{box-sizing:border-box;margin:0;padding:0}
  html,body{width:1200px;height:1200px;overflow:hidden;background:var(--bg);font-family:"Open Sans",sans-serif;color:var(--ink)}
  .sheet{position:relative;width:1200px;height:1200px}
  .page{position:absolute;width:357px;height:504px;background:var(--page);overflow:hidden;box-shadow:0 14px 14px -6px rgba(0,0,0,.35)}
  .row-1{top:26px}.row-2{top:608px}
  .col-1{left:28px}.col-2{left:422px}.col-3{left:817px}
  .page-label{position:absolute;width:357px;text-align:center;font-size:20px;color:var(--label);letter-spacing:.5px}
  .abs{position:absolute}
  .heading{position:absolute;left:18px;top:16px;font-size:14px;color:var(--blue);padding-bottom:2px;border-bottom:1.5px solid var(--blue-light);letter-spacing:.2px}
  .heading b{font-weight:700;color:var(--blue-dark)}
  .heading span{font-weight:400;color:var(--blue-light)}
  .body-text{position:absolute;left:18px;width:323px;font-size:7px;line-height:13px;text-align:justify;color:#333}
  .photo{position:absolute}
  .frame-tl,.frame-br{position:absolute;width:48px;height:48px;border-color:var(--blue-light);border-style:solid}
  .frame-tl{border-width:3px 0 0 3px}
  .frame-br{border-width:0 3px 3px 0}
  .footer-url{position:absolute;left:16px;bottom:11px;font-size:7.5px;letter-spacing:1.6px;color:#333}
  .page-no{position:absolute;right:16px;bottom:11px;font-size:7.5px;color:#fff}
  .swoosh{position:absolute;left:0;top:0}
  .brand{position:absolute;left:30px;top:14px;display:flex;align-items:center;gap:10px}
  .brand-dot{width:30px;height:30px;border-radius:50%;background:var(--blue)}
  .brand-name{font-size:29px;font-weight:600;color:var(--blue)}
  .cover-title{position:absolute;right:8px;text-align:right;color:#fff;font-weight:300;line-height:1}
  .sub-heading{position:absolute;left:18px;top:56px;font-size:7px;font-weight:700;color:var(--blue-dark);display:flex;align-items:center;gap:4px}
  .sub-heading i{display:inline-block;width:72px;height:1.5px;background:var(--blue)}
  .data-table{position:absolute;left:0;top:96px;width:357px;border-collapse:collapse;font-size:4.3px}
  .data-table th{background:var(--blue-dark);color:#fff;height:14px;font-weight:700;text-align:center}
  .data-table td{height:15.6px;text-align:center;color:#444}
  .data-table tr:nth-child(even) td{background:var(--row-alt)}
  .contact{position:absolute;left:0;width:357px;text-align:center;color:#fff}
</style>
</head>
<body>
<div class="sheet">

  <!-- Cover -->
  <section class="page row-1 col-1">
    <div class="brand"><div class="brand-dot"></div><div class="brand-name">KESTREL Polls</div></div>
    <svg class="swoosh" width="357" height="504" viewBox="0 0 357 504">
      <defs>
        <linearGradient id="towerTone" x1="0" y1="0" x2="1" y2="1">
          <stop offset="0" stop-color="#d9dde2"/><stop offset=".5" stop-color="#7d8590"/><stop offset="1" stop-color="#2c3138"/>
        </linearGradient>
      </defs>
      <rect role="img" aria-label="Upward view of a glass office tower" x="0" y="56" width="357" height="448" fill="url(#towerTone)"/>
      <path d="M0 470 C90 360 200 330 357 238 L357 504 L0 504Z" fill="#fff"/>
      <path d="M0 496 C80 400 200 365 357 342 L357 504 L0 504Z" fill="var(--blue-light)"/>
      <path d="M10 504 C90 412 210 375 357 356 L357 504Z" fill="var(--blue)"/>
    </svg>
    <div class="cover-title" style="top:382px;font-size:48px">EUISMOD</div>
    <div class="cover-title" style="top:436px;font-size:32px">AC MAGNA NEC</div>
    <div class="cover-title" style="top:467px;font-size:23px">LOREM EUISMOD CONGUE</div>
  </section>
  <div class="page-label" style="left:28px;top:550px">COVER PAGE</div>

  <!-- Page 01 -->
  <section class="page row-1 col-2">
    <h2 class="heading"><b>ABOUT KESTREL</b> <span>POLLS</span></h2>
    <p class="body-text" style="top:46px">KESTREL Polls make it easier to work with multiple sources of public opinion data. It does so by formatting variables for consistency and merging datasets together. The current merged dataset includes millions of respondents, covers most countries in the world, and extends back decades. This increased variation over time and space enables answering new research questions with greater reliability.</p>
    <div class="frame-tl" style="left:17px;top:139px"></div>
    <div class="photo" role="img" aria-label="Hands holding a smartphone over a laptop" style="left:22px;top:143px;width:141px;height:107px;background:linear-gradient(135deg,#8a7263,#c9a58e 55%,#5d5a5c)"></div>
    <div class="frame-br" style="left:120px;top:207px"></div>
    <div class="frame-tl" style="left:189px;top:139px"></div>
    <div class="photo" role="img" aria-label="Person typing on a laptop at a wooden desk" style="left:194px;top:143px;width:140px;height:107px;background:linear-gradient(135deg,#6b4a33,#b89a80 50%,#e3ddd6)"></div>
    <div class="frame-br" style="left:291px;top:207px"></div>
    <div class="frame-tl" style="left:17px;top:283px"></div>
    <div class="photo" role="img" aria-label="Office worker on the phone at a desk with a laptop and plants behind" style="left:22px;top:287px;width:311px;height:148px;background:linear-gradient(90deg,#6f6a60,#355a35 35%,#9aa48c 70%,#e6e4df)"></div>
    <div class="frame-br" style="left:291px;top:392px"></div>
    <svg class="swoosh" width="357" height="504"><path d="M262 504 C305 494 340 478 357 452 L357 504Z" fill="var(--blue)"/></svg>
    <div class="footer-url">www.kestrelpolls.org</div><div class="page-no">01</div>
  </section>
  <div class="page-label" style="left:422px;top:550px">PAGE - 01</div>

  <!-- Page 02 -->
  <section class="page row-1 col-3">
    <h2 class="heading"><b>ETIAM DICTUM</b> <span>URNA SAGITTIS</span></h2>
    <p class="body-text" style="top:46px">Variables are available at three levels of analysis within each corresponding dataset: respondent, country-survey, and county-year. At the respondent level, common variables are binary and result from dichotomizing different answer scales. Neutral and midpoint answers are consistently grouped with negative answers, meaning that respondent level variables focus on measuring the presence of what it measures rather than its absence.</p>
    <p class="body-text" style="top:125px">Variables are available at three levels of analysis within each corresponding dataset: respondent, country-survey, and county-year. At the respondent level, common variables are binary and result from dichotomizing different answer scales. Neutral and midpoint answers are consistently grouped with negative answers, meaning that respondent level variables focus on measuring the presence of what it measures rather than its absence.</p>
    <div class="frame-tl" style="left:17px;top:228px"></div>
    <div class="photo" role="img" aria-label="Hand on a laptop keyboard beside a notebook and mug" style="left:22px;top:232px;width:313px;height:203px;background:linear-gradient(120deg,#c9c0b3,#8b8379 45%,#3d4048 80%,#56677f)"></div>
    <div class="frame-br" style="left:293px;top:392px"></div>
    <svg class="swoosh" width="357" height="504"><path d="M262 504 C305 494 340 478 357 452 L357 504Z" fill="var(--blue)"/></svg>
    <div class="footer-url">www.kestrelpolls.org</div><div class="page-no">02</div>
  </section>
  <div class="page-label" style="left:817px;top:550px">PAGE - 02</div>

  <!-- Page 03 -->
  <section class="page row-2 col-1">
    <h2 class="heading"><b>KESTREL</b> <span>POLL DATASETS</span></h2>
    <div class="sub-heading">ETIAM DICTUM URNA SAGITTIS <i></i></div>
    <p class="body-text" style="top:81px">Variables are available at three levels of analysis within each corresponding dataset - Respondent, country-survey, and county-year. At the respondent level, common variables are binary and result from dichotomizing different answer scales. Neutral and midpoint answers are consistently grouped with negative answers, meaning that respondent level variables focus on measuring the presence of what it measures rather than its absence.</p>
    <svg class="abs" style="left:0;top:0" width="357" height="504">
      <g stroke="var(--blue-light)" stroke-width=".6" stroke-dasharray="1.5 1.5">
        <line x1="25" y1="253" x2="309" y2="253"/><line x1="25" y1="280" x2="268" y2="280"/>
        <line x1="25" y1="320" x2="186" y2="320"/><line x1="25" y1="346" x2="105" y2="346"/>
        <line x1="25" y1="366" x2="146" y2="366"/><line x1="309" y1="253" x2="309" y2="396"/>
      </g>
      <path d="M25 396 L64 372 L105 346 L146 366 L186 320 L227 290 L268 280 L309 253 L309 396Z" fill="#d6e7f4"/>
      <polyline points="25,396 64,372 105,346 146,366 186,320 227,290 268,280 309,253" fill="none" stroke="var(--blue)" stroke-width=".8"/>
      <g fill="var(--blue)">
        <circle cx="64" cy="372" r="2"/><circle cx="105" cy="346" r="2"/><circle cx="146" cy="366" r="2"/>
        <circle cx="186" cy="320" r="2"/><circle cx="227" cy="290" r="2"/><circle cx="268" cy="280" r="2"/><circle cx="309" cy="253" r="2"/>
      </g>
      <g stroke="var(--blue)" stroke-width="1.2">
        <line x1="25" y1="182" x2="25" y2="396"/><line x1="25" y1="396" x2="334" y2="396"/>
        <line x1="21" y1="234" x2="25" y2="234"/><line x1="21" y1="275" x2="25" y2="275"/>
        <line x1="21" y1="316" x2="25" y2="316"/><line x1="21" y1="357" x2="25" y2="357"/>
        <line x1="64" y1="396" x2="64" y2="400"/><line x1="105" y1="396" x2="105" y2="400"/>
        <line x1="146" y1="396" x2="146" y2="400"/><line x1="186" y1="396" x2="186" y2="400"/>
        <line x1="227" y1="396" x2="227" y2="400"/><line x1="268" y1="396" x2="268" y2="400"/>
        <line x1="309" y1="396" x2="309" y2="400"/>
      </g>
      <path d="M25 176 L22 184 L28 184Z M340 396 L332 393 L332 399Z" fill="var(--blue)"/>
      <path d="M262 504 C305 494 340 478 357 452 L357 504Z" fill="var(--blue)"/>
    </svg>
    <div class="footer-url">www.kestrelpolls.org</div><div class="page-no">03</div>
  </section>
  <div class="page-label" style="left:28px;top:1132px">PAGE - 03</div>

  <!-- Page 04 -->
  <section class="page row-2 col-2">
    <h2 class="heading"><b>QUISQUE RISUS</b> <span>MAGNA</span></h2>
    <p class="body-text" style="top:46px">Lorem ipsum dolor sit amet, consectetur adipiscing elit. Duis ut tortor vitae lorem venenatis rutrum.</p>
    <table class="data-table">
      <thead><tr><th>NO</th><th>CUSTOMER NAME</th><th>ITEMS</th><th>SUBJECT CODE</th><th>SUBJECT CODE</th></tr></thead>
      <tbody>
        <tr><td>1</td><td>Laura Bennet</td><td>Mauris laoreet commodo</td><td>Mauris laoreet commodo</td><td>Mauris laoreet commodo</td></tr>
        <tr><td>2</td><td>Laura Bennet</td><td>Mauris laoreet commodo</td><td>Mauris laoreet commodo</td><td>Mauris laoreet commodo</td></tr>
        <tr><td>3</td><td>Laura Bennet</td><td>Mauris laoreet commodo</td><td>Mauris laoreet commodo</td><td>Mauris laoreet commodo</td></tr>
        <tr><td>4</td><td>Laura Bennet</td><td>Mauris laoreet commodo</td><td>Mauris laoreet commodo</td><td>Mauris laoreet commodo</td></tr>
        <tr><td>5</td><td>Laura Bennet</td><td>Mauris laoreet commodo</td><td>Mauris laoreet commodo</td><td>Mauris laoreet commodo</td></tr>
        <tr><td>6</td><td>Laura Bennet</td><td>Mauris laoreet commodo</td><td>Mauris laoreet commodo</td><td>Mauris laoreet commodo</td></tr>
        <tr><td>7</td><td>Laura Bennet</td><td>Mauris laoreet commodo</td><td>Mauris laoreet commodo</td><td>Mauris laoreet commodo</td></tr>
      </tbody>
    </table>
    <div class="frame-tl" style="left:17px;top:294px"></div>
    <div class="photo" role="img" aria-label="Hand touching a glowing network of connected nodes" style="left:22px;top:298px;width:311px;height:138px;background:radial-gradient(circle at 30% 35%,#d9c8e8,#5f6f8e 30%,#263a55 70%,#1a2638)"></div>
    <div class="frame-br" style="left:291px;top:393px"></div>
    <svg class="swoosh" width="357" height="504"><path d="M262 504 C305 494 340 478 357 452 L357 504Z" fill="var(--blue)"/></svg>
    <div class="footer-url">www.kestrelpolls.org</div><div class="page-no">04</div>
  </section>
  <div class="page-label" style="left:422px;top:1132px">PAGE - 04</div>

  <!-- Back page -->
  <section class="page row-2 col-3">
    <svg class="swoosh" width="357" height="504">
      <defs>
        <linearGradient id="gearTone" x1="0" y1="0" x2="1" y2="1">
          <stop offset="0" stop-color="#5a5f66"/><stop offset=".6" stop-color="#9a9ea4"/><stop offset="1" stop-color="#d8d9db"/>
        </linearGradient>
      </defs>
      <rect role="img" aria-label="Hands holding a tablet beneath metal gears" x="0" y="0" width="357" height="240" fill="url(#gearTone)"/>
      <path d="M0 286 C60 200 150 150 357 140 L357 504 L0 504Z" fill="#fff"/>
      <path d="M0 296 C70 210 160 162 357 154 L357 504 L0 504Z" fill="var(--blue-light)"/>
      <path d="M0 312 C80 220 170 172 357 164 L357 504 L0 504Z" fill="var(--blue)"/>
      <g fill="none" stroke="#fff" stroke-width="1.2">
        <path d="M142 320 c2-4 5-5 6-4 l2 3 c0 1-2 2-2 3 1 2 3 4 5 5 1 0 2-2 3-2 l3 2 c1 1 0 4-4 6 -6 1-14-8-13-13z"/>
        <rect x="167" y="317" width="16" height="11"/><path d="M167 317 l8 6 8-6"/>
        <circle cx="206" cy="322.5" r="7"/><ellipse cx="206" cy="322.5" rx="3" ry="7"/><line x1="199" y1="322.5" x2="213" y2="322.5"/>
      </g>
    </svg>
    <div class="contact" style="top:260px;font-size:28px;font-weight:300">CONTACT US</div>
    <div class="contact" style="top:346px;font-size:13px">555.014.2290</div>
    <div class="contact" style="top:374px;font-size:13px">info@kestrelpolls.org</div>
    <div class="contact" style="top:402px;font-size:13px">www.kestrelpolls.org</div>
    <div class="contact" style="top:482px;font-size:7.5px;letter-spacing:1.4px">Copyright © 2018 KESTREL Polls All right reserved</div>
  </section>
  <div class="page-label" style="left:817px;top:1132px">BACK PAGE</div>

</div>
</body>
</html>
```